Website design for recruitment solutions

We connect top talents to fast growing employers in Asia. We need to revamp our existing website (currently outdated) and also add more pages to make it more informative for talents and employers.
We need final design output to be for both desktop and mobile devices. The final design output must come with all specifications so it's easier for our dev team to implement. We have a detailed mockup but we expect the design to be significantly changed by the final output. We want the pages to look aesthetic, modern and professional.
Number of Pages Required
5+ page
Requirements
Must have
- - To have Pages design for desktop+mobile. Need to take into account intermediate resolutions like 1365px\1023px\767px\479px, especially if mobile/desktop design differs considerably. Design should be repeatable (between pages), suitable for block-layout.
Nice to have
- In terms of receiving files, we usually work with designers who can deliver files in Figma or Sketch with export to Figma. If in PSD format - please export to Zeplin or Avocode, otherwise will be difficult to open

```html
<!DOCTYPE html>
<html lang="en">
<head>
<meta charset="utf-8">
<title>Talentra — Recruitment Partner</title>
<link href="https://fonts.googleapis.com/css2?family=Raleway:wght@400;500;600;700&display=swap" rel="stylesheet">
<style>
:root{
  --blue:#1f57a8;
  --blue-deep:#1b4f9e;
  --green:#6ac995;
  --teal:#3f8fa0;
  --red:#f50d0d;
  --slate:#56739b;
  --mint:#68c893;
  --ink:#1a1a1a;
  --muted:#555;
  --hero-text:#a9e3bf;
  --card-border:#e3e3e3;
}
*{box-sizing:border-box;margin:0;padding:0}
html,body{width:686px;height:1200px;overflow:hidden;background:#fff}
body{font-family:'Raleway',sans-serif;color:var(--ink);position:relative}
.abs{position:absolute}
.hero-bg,.testimonials-bg{position:absolute;left:0;top:0}
.nav-brand{left:73px;top:25px;font-size:8.5px;font-weight:600;letter-spacing:1.4px;color:#e8f2f5}
.nav-link{top:26px;font-size:8.5px;font-weight:600;letter-spacing:1px;color:#eef7f3}
.nav-rule{left:66px;top:42px;width:563px;height:1px;background:rgba(255,255,255,.45)}
.btn-register{background:var(--red);color:#fff;font-weight:600;letter-spacing:1px;display:flex;align-items:center;justify-content:center;box-shadow:0 1px 3px rgba(0,0,0,.25)}
.btn-login{background:#fff;color:var(--ink);font-weight:700;letter-spacing:1px;display:flex;align-items:center;justify-content:center;box-shadow:0 1px 3px rgba(0,0,0,.25)}
.hero-title{left:0;width:686px;top:84px;text-align:center;font-size:30px;line-height:38px;font-weight:400;color:var(--hero-text);letter-spacing:.2px}
.btn-start{left:300px;top:185px;width:95px;height:28px;background:#fff;border:1px solid var(--mint);font-size:8.5px;font-weight:500;display:flex;align-items:center;justify-content:center;box-shadow:0 2px 4px rgba(0,0,0,.2)}
.feature{background:#fdfcfd;border:1px solid var(--card-border);text-align:center}
.feature-icon{position:absolute;left:50%;transform:translateX(-50%);width:72px;height:72px;border-radius:50%;background:#ececec;box-shadow:2px 3px 4px rgba(0,0,0,.18);display:flex;align-items:center;justify-content:center}
.feature-icon .ring{width:66px;height:66px;border-radius:50%;border:2.5px solid;display:flex;align-items:center;justify-content:center;background:#ededed}
.feature h3{position:absolute;left:0;width:100%;font-size:11.5px;font-weight:500;letter-spacing:.3px}
.feature p{position:absolute;left:8px;right:8px;font-size:7.6px;line-height:11px;color:var(--muted);letter-spacing:.3px}
.testimonial{background:#fff;box-shadow:0 2px 4px rgba(0,0,0,.2);overflow:hidden}
.testimonial svg.shape{position:absolute;left:0;top:0}
.avatar{position:absolute;left:26px;top:15px;width:48px;height:48px;border-radius:50%}
.t-name{position:absolute;left:84px;top:37px;font-size:7.5px;color:var(--ink)}
.t-role{position:absolute;left:88px;top:48px;font-size:6.5px;color:#888}
.t-quote{position:absolute;left:8px;right:8px;top:91px;text-align:center;font-size:7.6px;line-height:11px;color:#333}
.dot{width:5px;height:5px;border-radius:50%;border:1px solid var(--blue);top:968px}
.footer{left:0;top:1004px;width:686px;height:196px;background:linear-gradient(200deg,var(--green) 0%,var(--teal) 45%,var(--blue-deep) 100%)}
.f-brand{left:62px;top:1037px;font-size:8.5px;font-weight:600;letter-spacing:1.6px;color:#e9f3f1}
.f-about{left:62px;top:1053px;width:160px;font-size:6.5px;line-height:9.6px;color:#e3efee}
.f-head{top:1063px;font-size:8.5px;font-weight:500;letter-spacing:1.6px;color:#eef7f3}
.f-link{font-size:7.6px;letter-spacing:.5px;color:#e6f1f2}
.f-social{top:1111px;width:14px;height:14px;border-radius:2px;background:#fff}
.f-copy{left:57px;top:1150px;font-size:7.2px;font-weight:700;color:#fff}
.f-legal{font-size:5px;line-height:6.7px;font-weight:700;color:#fff;text-align:center}
</style>
</head>
<body>

<!-- Hero -->
<svg class="hero-bg" width="686" height="340" viewBox="0 0 686 340" role="img" aria-label="Hero background: business people with hexagon icons of travel, finance and teamwork in blue-green tones">
  <defs>
    <linearGradient id="heroGrad" x1="0" y1="1" x2="1" y2="0">
      <stop offset="0" stop-color="#1e53a6"/>
      <stop offset=".45" stop-color="#2f7da8"/>
      <stop offset="1" stop-color="#6ccb95"/>
    </linearGradient>
  </defs>
  <path d="M0 0H686V250Q343 410 0 250Z" fill="url(#heroGrad)"/>
  <path d="M0 250Q343 410 686 250" fill="none" stroke="#fff" stroke-width="2"/>
  <path d="M0 254Q343 416 686 254" fill="none" stroke="#d8d8d8" stroke-width="1"/>
</svg>

<div class="abs nav-brand">TALENTRA</div>
<div class="abs nav-link" style="left:214px">How we work</div>
<div class="abs nav-link" style="left:295px">Browse Jobs</div>
<div class="abs nav-link" style="left:372px">Employers</div>
<div class="abs nav-link" style="left:441px">About Us</div>
<div class="abs nav-rule"></div>
<div class="abs btn-register" style="left:502px;top:20px;width:55px;height:22px;font-size:8.5px">Register</div>
<div class="abs btn-login" style="left:574px;top:20px;width:55px;height:22px;font-size:8.5px">Log In</div>

<h1 class="abs hero-title">We&nbsp; connect top&nbsp; talents&nbsp; into fast<br>growing employers&nbsp; in&nbsp; Asia.</h1>
<div class="abs btn-start">Get Started</div>

<!-- Features -->
<section class="abs feature" style="left:66px;top:350px;width:163px;height:199px">
  <div class="feature-icon" style="top:4px">
    <div class="ring" style="border-color:var(--slate)">
      <svg width="30" height="30" viewBox="0 0 24 24" fill="none" stroke="#111" stroke-width="2" stroke-linecap="round"><path d="M10 13a5 5 0 0 0 7.5.5l3-3a5 5 0 0 0-7-7l-1.7 1.7"/><path d="M14 11a5 5 0 0 0-7.5-.5l-3 3a5 5 0 0 0 7 7l1.7-1.7"/></svg>
    </div>
  </div>
  <h3 style="top:96px">Smart Connections</h3>
  <p style="top:122px">It's&nbsp; the&nbsp; quality of the&nbsp; connection that&nbsp; matters Our role matching algorithms and talent&nbsp; managers work around the clock to find opportunities suit able to your unique&nbsp; profil e .</p>
</section>

<section class="abs feature" style="left:268px;top:398px;width:163px;height:225px">
  <div class="feature-icon" style="top:9px">
    <div class="ring" style="border-color:#c8151b">
      <svg width="30" height="30" viewBox="0 0 24 24" fill="none" stroke="#111" stroke-width="2" stroke-linejoin="round"><path d="M3 4h18l-7 8.5V20l-4-2v-5.5Z"/></svg>
    </div>
  </div>
  <h3 style="top:99px">Critical insights</h3>
  <p style="top:124px">Our close interactions with candidates and employers have helped us create a comprehensive database of companies,talents and&nbsp; skills with Talentra, you will&nbsp; gain full access to timely intel&nbsp; to help you make the right career<br><span style="display:inline-block;margin-top:6px">decision .</span></p>
</section>

<section class="abs feature" style="left:474px;top:354px;width:160px;height:216px">
  <div class="feature-icon" style="top:6px">
    <div class="ring" style="border-color:#22c06a">
      <svg width="30" height="30" viewBox="0 0 24 24" fill="none" stroke="#111" stroke-width="2" stroke-linecap="round" stroke-linejoin="round"><circle cx="9" cy="8" r="4"/><path d="M2 21v-1a6 6 0 0 1 6-6h2"/><path d="M15 13l2 2 4-4"/></svg>
    </div>
  </div>
  <h3 style="top:88px">People First</h3>
  <p style="top:112px;font-size:7.4px">we take the time to really understand you holistically as a person to maximize your potential . As your career counselor , we provide maximum transparency and feedback throughout the process</p>
</section>

<!-- Testimonials -->
<svg class="testimonials-bg" style="top:0" width="686" height="1004" viewBox="0 0 686 1004" aria-hidden="true">
  <defs>
    <linearGradient id="greyGrad" x1="0" y1="0" x2="0" y2="1">
      <stop offset="0" stop-color="#d9d9d9"/>
      <stop offset="1" stop-color="#ffffff"/>
    </linearGradient>
  </defs>
  <path d="M0 733Q343 573 686 733V1004H0Z" fill="url(#greyGrad)"/>
</svg>

<article class="abs testimonial" style="left:104px;top:750px;width:149px;height:180px">
  <svg class="shape" width="149" height="180" viewBox="0 0 149 180"><path d="M0 0H122Q112 28 72 32Q22 38 0 68Z" fill="var(--red)"/><path d="M149 125Q144 172 84 180H149Z" fill="var(--red)"/></svg>
  <div class="avatar" role="img" aria-label="Portrait photo of Nadia Harlow" style="background:#4a3a34"></div>
  <div class="t-name">Nadia Harlow</div>
  <div class="t-role">Trader</div>
  <p class="t-quote">Aliqua qui cupidatat cillum ipsum. Pariatur duis labore enim voluptate excepteur commodo eiusmod duis ad.v Et laborum voluptate excepteur mini in officia sit irure</p>
</article>

<article class="abs testimonial" style="left:298px;top:750px;width:144px;height:180px">
  <svg class="shape" width="144" height="180" viewBox="0 0 144 180"><path d="M0 0H120Q110 28 70 32Q20 38 0 68Z" fill="var(--slate)"/><path d="M144 125Q139 172 80 180H144Z" fill="var(--slate)"/></svg>
  <div class="avatar" role="img" aria-label="Portrait photo of Marcus Odell" style="background:#3a2a22;left:24px"></div>
  <div class="t-name" style="left:84px;font-size:7px">Marcus Odell</div>
  <div class="t-role">Trader</div>
  <p class="t-quote" style="top:89px">Aliqua qui cupidatat cillum ipsum. Pariatur duis labore enim voluptate excepteur commodo eiusmod duis ad.v Et laborum voluptate excepteur minim in officia sit irure</p>
</article>

<article class="abs testimonial" style="left:491px;top:750px;width:145px;height:180px">
  <svg class="shape" width="145" height="180" viewBox="0 0 145 180"><path d="M0 0H120Q110 28 70 32Q20 38 0 68Z" fill="var(--mint)"/><path d="M145 125Q140 172 80 180H145Z" fill="var(--mint)"/></svg>
  <div class="avatar" role="img" aria-label="Portrait photo of Helena Price" style="background:#d9b98a;left:24px"></div>
  <div class="t-name" style="left:86px;font-size:7px">Helena Price</div>
  <div class="t-role">Trader</div>
  <p class="t-quote" style="top:89px">Aliqua qui cupidatat cillum ipsum. Pariatur duis labore enim voluptate excepteur commodo eiusmod duis ad.v Et laborum voluptate excepteur minimv in officia sit irure</p>
</article>

<div class="abs dot" style="left:334px;background:var(--blue)"></div>
<div class="abs dot" style="left:354px"></div>
<div class="abs dot" style="left:375px"></div>

<!-- Footer -->
<footer class="abs footer" role="img" aria-label="Footer background: hexagon business icons over a blue-green gradient"></footer>
<div class="abs f-brand">TALENTRA</div>
<p class="abs f-about">TALENTRA&nbsp; is&nbsp; a modern&nbsp; recruimeent partner for high potential technology and finance talents .we work closely with hedge funds , systematic trading and Fin Tech employers experiencing hyper growth in Asia</p>
<div class="abs f-social" style="left:62px"></div>
<div class="abs f-social" style="left:85px;border-radius:50%"></div>
<div class="abs btn-register" style="left:109px;top:1109px;width:55px;height:22px;font-size:8.5px">Register</div>
<div class="abs f-copy">TALENTRA 2012-2020 All rights reserved</div>

<div class="abs f-head" style="left:269px">TALENTS</div>
<div class="abs f-link" style="left:268px;top:1078px">How We Work</div>
<div class="abs f-link" style="left:268px;top:1093px">Browse jobs</div>

<div class="abs f-head" style="left:354px;top:1062px">EMPLOYERS</div>
<div class="abs f-link" style="left:361px;top:1078px">Why Talentra</div>

<div class="abs f-head" style="left:460px;top:1062px">About Us</div>
<div class="abs f-link" style="left:455px;top:1078px">About Talentra</div>
<div class="abs f-link" style="left:446px;top:1092px">Working at Talentra</div>

<div class="abs f-legal" style="left:234px;top:1143px;width:180px">Northgate Staffing Limited ( EA License No. 40217)<br>Suite 14, Level 6, Harbour Point Tower B,<br>22 Lantern Road,<br>Kowloon, HONG KONG</div>
<div class="abs f-legal" style="left:450px;top:1143px;width:180px">Talentra Pte. Ltd . (License No. 2046318)<br>88 Marina Way , #12-03 Bayfront Hub, Singapore 018956</div>

</body>
</html>
```